Tarvel Ridge LLC

Need Professional Business cards for New Investment Fund

Target Market(s)

High Quality investors

Industry/Entity Type

Financial

Contact Information for Business Card

Phone Number +1 555 284 6193
Name Pavel Orlinsky
Title Fund Manager
email po@FundTarvel.example
Website www.FundTarvel.example

Colors

Designer to choose colors to be used in the design.

Requirements
Must have
• Must have our Logo and all of the above. Must be made so lettering and loge can be raised

```html
<!DOCTYPE html>
<html lang="en">
<head>
<meta charset="utf-8">
<title>Tarvel Ridge LLC – Business Card</title>
<link rel="stylesheet" href="https://fonts.googleapis.com/css2?family=Jost:wght@400;500;600;700&family=Arimo:wght@400&display=swap">
<style>
  :root{
    --bg:#1c1c1c;
    --green:#4dbb45;
    --green-light:#76cc6a;
    --charcoal:#444b47;
    --ink:#3a3d3b;
    --paper:#ffffff;
    --faint:#efefef;
  }
  *{margin:0;padding:0;box-sizing:border-box}
  html,body{width:1200px;height:1200px;overflow:hidden;background:var(--bg)}
  .canvas{position:relative;width:1200px;height:1200px}
  .card{position:absolute;left:180px;width:840px;height:480px;overflow:hidden;box-shadow:0 10px 30px rgba(0,0,0,.5)}
  /* back side */
  .card-back{top:90px}
  .card-back .pattern{position:absolute;inset:0;
    background:linear-gradient(180deg,var(--green-light) 0%,#5a8a57 28%,#4a5450 48%,#577a55 66%,var(--green) 100%)}
  .back-mark{position:absolute;left:50%;top:50%;transform:translate(-50%,-50%);display:flex;align-items:center;gap:14px;white-space:nowrap}
  .mark-square{flex:none;width:22px;height:22px;background:var(--paper)}
  .back-mark .mark-name{font:600 34px/1 'Jost',sans-serif;color:var(--paper);letter-spacing:2px}
  /* front side */
  .card-front{top:630px;background:var(--paper)}
  .watermark{position:absolute;left:30px;top:14px;font:700 110px/1 'Jost',sans-serif;color:var(--faint);letter-spacing:2px}
  .company{position:absolute;left:110px;top:92px;white-space:nowrap}
  .company-name{font:700 32px/1 'Jost',sans-serif;color:var(--ink);letter-spacing:.5px}
  .company-name .accent{color:var(--green)}
  .company-tag{margin-top:10px;font:400 15px/1 'Jost',sans-serif;color:var(--green);letter-spacing:12px}
  .front-mark{position:absolute;right:70px;top:130px;display:flex;align-items:center;gap:12px;white-space:nowrap}
  .front-mark .mark-square{width:20px;height:20px;background:var(--green)}
  .front-mark .mark-name{font:600 24px/1 'Jost',sans-serif;color:var(--charcoal);letter-spacing:2px}
  .rule-green{position:absolute;left:110px;top:300px;width:430px;height:2px;background:var(--green)}
  .rule-dark{position:absolute;left:550px;top:318px;width:220px;height:2px;background:var(--charcoal)}
  .person{position:absolute;left:110px;top:318px}
  .person-name{font:600 30px/1 'Jost',sans-serif;color:var(--ink);letter-spacing:1px}
  .person-title{margin-top:8px;font:400 22px/1 'Jost',sans-serif;color:var(--green);letter-spacing:3px}
  .contacts{position:absolute;right:70px;top:340px;list-style:none}
  .contacts li{display:flex;justify-content:flex-end;align-items:center;gap:14px;font:400 20px/1 'Arimo',sans-serif;color:var(--ink);margin-bottom:10px}
  .contacts svg{width:20px;height:20px;fill:none;stroke:var(--green);stroke-width:2}
</style>
</head>
<body>
<div class="canvas">
  <section class="card card-back">
    <div class="pattern" role="img" aria-label="Green gradient field with a faint repeating brand pattern"></div>
    <div class="back-mark">
      <span class="mark-square"></span>
      <span class="mark-name">TARVEL RIDGE</span>
    </div>
  </section>

  <section class="card card-front">
    <div class="watermark" aria-hidden="true">TARVEL</div>
    <div class="company">
      <h1 class="company-name"><span class="accent">TARVEL RIDGE</span> LLC</h1>
      <p class="company-tag">INVESTMENT FUND</p>
    </div>
    <div class="front-mark">
      <span class="mark-square"></span>
      <span class="mark-name">TARVEL RIDGE</span>
    </div>
    <div class="rule-green"></div>
    <div class="rule-dark"></div>
    <div class="person">
      <h2 class="person-name">PAVEL ORLINSKY</h2>
      <p class="person-title">FUND MANAGER</p>
    </div>
    <ul class="contacts">
      <li>+1 555 284 6193
        <svg viewBox="0 0 24 24"><path d="M5 3h4l2 5-3 2a12 12 0 0 0 6 6l2-3 5 2v4a2 2 0 0 1-2 2A18 18 0 0 1 3 5a2 2 0 0 1 2-2z" fill="var(--green)" stroke="none"/></svg>
      </li>
      <li>po@FundTarvel.example
        <svg viewBox="0 0 24 24"><rect x="2" y="5" width="20" height="14"/><path d="M2 5l10 8 10-8"/></svg>
      </li>
      <li>www.FundTarvel.example
        <svg viewBox="0 0 24 24"><circle cx="12" cy="12" r="10"/><ellipse cx="12" cy="12" rx="4" ry="10"/><path d="M2 12h20M4 7h16M4 17h16"/></svg>
      </li>
    </ul>
  </section>
</div>
</body>
</html>
```